Walt's 85th Birthday Invitation

Invitation to celebrate Walt's turning 85. OKTOBERFEST with fall colors & maybe some beer steins/autumn leaves/happy/fun images. Below are my thoughts for the wording but I need someone to bring it to life.
It's not just a party
it's an
OKTOBERFEST
to celebrate
Picture of Walt
Walt's 85th birthday

Saturday, October 25, 2014

at the Lindmoor Ale Court
Pelorvale
4127 Denbury Ave.
Garden Grove, CA 92871

Cocktails at 6 Dinner at 7
Dancing & Partying till 10:00

No birthday gifts please.
Please consider a gift to PelorVale!
Casual Attire

I would like this on a horizontal 5x7 flat card that will fit the envelopes you have. The text & spacing can be adjusted. This is just a rough draft. Thank you for your help! I will need 150 invitations with envelopes.

OktoberFest

```html
<!DOCTYPE html>
<html lang="en">
<head>
<meta charset="utf-8">
<title>Walt's 85th Birthday Oktoberfest Invitation</title>
<link rel="stylesheet" href="https://fonts.googleapis.com/css2?family=Bebas+Neue&family=Josefin+Sans:wght@300;400&family=UnifrakturCook:wght@700&display=swap">
<style>
  :root {
    --page: #ffffff;
    --ink: #111111;
    --glow: #ffffff;
    --sage: #a9ac90;
    --teal: #3ebfa9;
    --wheat: #b3a78c;
    --salmon: #ec8a6f;
    --tan: #d29a82;
    --cream: #fff8f2;
    --lime: #d6e09c;
  }
  * { box-sizing: border-box; margin: 0; padding: 0; }
  html, body {
    width: 1200px; height: 1000px; overflow: hidden;
    background: var(--page);
  }
  .invitation {
    position: absolute; left: 144px; top: 174px;
    width: 912px; height: 652px;
    background:
      radial-gradient(circle at 100% 0%, var(--cream) 0%, rgba(255,248,242,0.7) 10%, rgba(255,248,242,0) 28%),
      linear-gradient(to top right, var(--lime) 0%, var(--teal) 24%, var(--sage) 42%, var(--wheat) 50%, var(--salmon) 66%, var(--tan) 80%, #f4c6b2 92%, var(--cream) 100%);
    color: var(--ink);
    font-family: "Bebas Neue", sans-serif;
  }
  .invitation > * { position: absolute; }
  .teaser {
    top: 14px; left: 0; width: 100%; text-align: center;
    font-size: 30px; letter-spacing: 5px; line-height: 1;
  }
  .festival-title { left: 0; top: 0; width: 912px; height: 240px; }
  .festival-title text {
    font-family: "UnifrakturCook", cursive; font-weight: 700;
    font-size: 80px; fill: var(--ink);
  }
  .celebrate {
    top: 212px; left: 0; width: 100%;
    display: flex; justify-content: center; align-items: center; gap: 12px;
    font-size: 40px; letter-spacing: 5px; line-height: 1;
  }
  .celebrate .rule {
    width: 120px; height: 8px;
    border-top: 2px solid var(--ink); border-bottom: 2px solid var(--ink);
  }
  .honoree {
    top: 264px; left: 0; width: 100%; text-align: center;
    font-size: 66px; letter-spacing: 6px; line-height: 1;
  }
  .honoree small { font-size: 36px; letter-spacing: 3px; }
  .divider { left: 218px; width: 476px; height: 1px; background: var(--ink); }
  .divider.upper { top: 335px; }
  .divider.lower { top: 406px; }
  .divider.footer { left: 18px; width: 852px; top: 606px; }
  .event-date {
    top: 360px; left: 0; width: 100%; text-align: center;
    font-family: "Josefin Sans", sans-serif; font-weight: 300;
    font-size: 21px; letter-spacing: 5px; line-height: 1;
  }
  .venue, .schedule {
    font-size: 31px; letter-spacing: 2px; line-height: 45.5px;
    text-align: center;
    text-shadow: 1px 1px 0 var(--glow), -1px 0 0 var(--glow), 0 -1px 0 var(--glow), 2px 2px 0 var(--glow);
  }
  .venue { top: 418px; left: 40px; width: 340px; }
  .schedule { top: 468px; left: 522px; width: 340px; }
  .separators { left: 440px; top: 424px; width: 32px; height: 140px; }
  .footnote {
    top: 618px; font-size: 23px; letter-spacing: 1.6px; line-height: 1;
    text-shadow: 1px 1px 0 var(--glow);
  }
  .footnote.gifts { left: 16px; }
  .footnote.attire { right: 18px; }
</style>
</head>
<body>
  <main class="invitation">
    <p class="teaser">It's not just a party... it's an</p>

    <svg class="festival-title" viewBox="0 0 912 240" aria-label="Oktoberfest">
      <path id="title-arc" d="M 230 196 Q 456 150 682 196" fill="none"/>
      <text><textPath href="#title-arc" startOffset="50%" text-anchor="middle" textLength="448" lengthAdjust="spacingAndGlyphs">oktoberfest</textPath></text>
    </svg>

    <div class="celebrate">
      <span class="rule"></span>
      <span>to celebrate</span>
      <span class="rule"></span>
    </div>

    <h1 class="honoree">Walt's 85<small>th</small> Birthday</h1>

    <div class="divider upper"></div>
    <p class="event-date">SATURDAY, OCTOBER 25, 2014</p>
    <div class="divider lower"></div>

    <address class="venue" style="font-style: normal;">
      At the Lindmoor Ale<br>
      Court Pelorvale<br>
      4127 Denbury Avenue<br>
      Garden Grove, CA 92871
    </address>

    <svg class="separators" viewBox="0 0 32 140" aria-hidden="true">
      <polygon points="16,2 28,14 16,26 4,14" fill="#111"/>
      <polygon points="16,40 28,52 16,64 4,52" fill="#111"/>
      <polygon points="16,76 28,88 16,100 4,88" fill="#111"/>
      <polygon points="16,114 28,126 16,138 4,126" fill="#111"/>
    </svg>

    <p class="schedule">
      Cocktails at 6 Dinner at 7<br>
      Dancing &amp; Partying 'til 10
    </p>

    <div class="divider footer"></div>
    <p class="footnote gifts">No birthday gifts; please consider a gift to Pelorvale</p>
    <p class="footnote attire">Casual attire</p>
  </main>
</body>
</html>
```